Firm of surveyors needs a professional yet friendly looking flyer

Our company offers help to landlords who have a phone mast on their property. We help them to negotiate the best rent and lease terms. There are so many landlords who don't seek professional advice because they don't know it's available. We want to send them a flyer which is informative, looks professional but also friendly so it prompts them to call us. I have attached the wording and some pictures but have more I can send but they were too large to attach.

Target Market(s)

Ranges from farmers to large corporations and land owners

Industry/Entity Type

Surveyor

Font styles to use
Sans Serif

Colors
acd136
9bcb3c
000000
ffffff
606060
848484

Requirements
Must have
• Must be clear, must give a professional look, must include pictures, must include our logo, must use our colour scheme (or variations of it). Ideally, I would like a try-fold design if possible.
Nice to have
• I would like there to be stand out lines to catch the readers eye (I have included some on the wording document). I would like a clean and modern design
Should not have
• Should not be too fussy

```html
<!DOCTYPE html>
<html lang="en">
<head>
<meta charset="utf-8">
<title>The Signal Site Company – Landlord Tri-fold</title>
<link rel="stylesheet" href="https://fonts.googleapis.com/css2?family=Roboto:ital,wght@0,300;0,400;0,500;0,700;1,700&family=Roboto+Condensed:ital,wght@0,400;0,700;1,700&display=swap">
<style>
:root{
  --page:#e4e5e7;
  --blue-deep:#2a5aa8;
  --blue-mid:#3d7cc9;
  --blue-sky:#7fb2e4;
  --green:#5b9b3b;
  --green-bright:#9bcb3c;
  --green-lime:#acd136;
  --green-ink:#3f8a2e;
  --green-dark:#1f5420;
  --ink:#000000;
  --grey-dark:#606060;
  --grey-mid:#848484;
  --grey-light:#dcdcdc;
  --white:#ffffff;
}
*{box-sizing:border-box;margin:0;padding:0}
html,body{width:1200px;height:1200px;overflow:hidden}
body{background:var(--page);font-family:"Roboto",Arial,sans-serif;color:var(--ink);position:relative}

.sheet{position:absolute;width:736px;height:571px;display:flex;box-shadow:0 6px 18px rgba(0,0,0,.25)}
.sheet--outside{left:34px;top:26px}
.sheet--inside{left:422px;top:614px}
.panel{position:relative;width:245px;height:100%;overflow:hidden}
.panel:last-child{width:246px}

/* Outside: services */
.services{background:linear-gradient(180deg,var(--blue-deep) 0%,var(--blue-mid) 45%,var(--blue-sky) 100%)}
.services__photo{position:absolute;left:0;right:0;top:215px;bottom:0;
  background:linear-gradient(180deg,rgba(255,255,255,0) 0%,rgba(210,220,235,.25) 60%,rgba(190,198,210,.75) 88%,#b9c0c8 100%)}
.services__title{position:absolute;left:31px;top:22px;font-weight:300;font-size:28px;color:var(--white);letter-spacing:.5px}
.services__list{position:absolute;left:33px;top:66px;list-style:none}
.services__list li{display:flex;align-items:center;gap:6px;color:var(--white);font-size:11.4px;line-height:16.6px}
.services__list svg{width:10px;height:10px;flex:none}

/* Outside: advice */
.advice{background:var(--grey-light)}
.advice__top{position:absolute;left:0;top:0;width:100%;height:395px;background:var(--green)}
.advice__headline{position:absolute;left:10px;right:10px;top:50px;text-align:center;color:var(--white);font-weight:300;font-size:21px;line-height:24.6px}
.advice__brand{position:absolute;left:0;right:0;top:262px;display:flex;justify-content:center}
.advice__prompt{position:absolute;left:8px;right:8px;top:320px;text-align:center;color:var(--white);font-size:13.4px;line-height:16.5px}
.advice__prompt strong{display:block;font-family:"Roboto Condensed",sans-serif;font-style:italic;font-weight:700;font-size:13.4px;color:var(--green-lime)}
.contact{position:absolute;left:0;right:0;top:409px;text-align:center;font-size:8.8px;line-height:11px;color:var(--ink)}
.contact__name{font-size:11px;line-height:13px}
.contact p+p{margin-top:11px}

/* Brand lockup */
.brand{display:flex;align-items:center;gap:7px;font-family:"Roboto Condensed",sans-serif;font-weight:700;font-size:19px;line-height:1;color:var(--green-dark)}
.brand__dot{width:14px;height:14px;border-radius:50%;background:currentColor;flex:none}
.brand--sky{color:var(--green-ink)}

/* Outside: cover */
.cover__photo{position:absolute;inset:0;
  background:linear-gradient(180deg,#eef3fb 0%,#c4d9f0 22%,#8eb6e0 48%,#a9c7e6 62%,#8fb46a 70%,#6f9b45 84%,#557d32 100%)}
.cover__brand{position:absolute;left:32px;top:98px}
.cover__tagline{position:absolute;left:34px;top:268px;font-weight:300;font-size:18px;line-height:22px;color:#1e2a38}
.cover__web{position:absolute;left:0;right:0;bottom:28px;text-align:center;font-weight:300;font-size:13px;color:var(--white)}

/* Inside */
.about{background:var(--green)}
.about__title{position:absolute;left:24px;top:26px;font-weight:300;font-size:31px;color:var(--white);letter-spacing:.5px}
.text{position:absolute;left:24px;width:204px;font-size:9.9px;line-height:12.1px;text-align:justify;hyphens:auto;color:var(--ink)}
.about .text{color:#102010}
.about__lead{top:73px;font-family:"Roboto Condensed",sans-serif;font-weight:700;font-size:12px;line-height:14px}
.about__p1{top:145px}
.about__p2{top:284px}

.middle{background:var(--white)}
.middle .text{left:14px;width:218px}
.middle__intro{top:28px}
.middle__photo{position:absolute;left:0;width:100%;top:142px;height:214px;background:linear-gradient(135deg,#7aa0c2 0%,#b9c7a4 45%,#d8c48a 100%)}
.middle__inset{position:absolute;right:3px;top:244px;width:118px;height:118px;border-radius:50%;border:4px solid var(--white);background:radial-gradient(circle at 40% 35%,#4f8fd6,#1f5aa8)}
.heading{position:absolute;font-family:"Roboto Condensed",sans-serif;font-weight:400;color:var(--green-ink);font-size:19px;line-height:22px}
.middle__heading{left:14px;top:372px}
.middle__sell{top:400px}

.market{background:linear-gradient(90deg,#ececec 0%,var(--white) 25%)}
.market .text{left:16px;width:214px}
.market__h1{left:16px;top:27px}
.market__p1{top:52px}
.market__h2{left:16px;top:181px}
.market__p2{top:232px}
.market__law{top:442px;font-family:"Roboto Condensed",sans-serif;font-weight:700;font-size:12.4px;line-height:15px;text-align:left}
.market__law em{font-style:italic;font-size:10px;line-height:12.1px;color:var(--green-dark)}
</style>
</head>
<body>

<section class="sheet sheet--outside">
  <div class="panel services">
    <div class="services__photo" role="img" aria-label="Photo of a telecoms mast with antennas against a blue sky on a rooftop"></div>
    <h2 class="services__title">OUR SERVICES</h2>
    <ul class="services__list">
      <li><svg viewBox="0 0 10 10"><path d="M1 5.5l2.5 2.5L9 1.5" fill="none" stroke="#fff" stroke-width="2"/></svg>Rent Reviews</li>
      <li><svg viewBox="0 0 10 10"><path d="M1 5.5l2.5 2.5L9 1.5" fill="none" stroke="#fff" stroke-width="2"/></svg>Lease Renewals</li>
      <li><svg viewBox="0 0 10 10"><path d="M1 5.5l2.5 2.5L9 1.5" fill="none" stroke="#fff" stroke-width="2"/></svg>Network Consolidation Issues</li>
      <li><svg viewBox="0 0 10 10"><path d="M1 5.5l2.5 2.5L9 1.5" fill="none" stroke="#fff" stroke-width="2"/></svg>Site Shares</li>
      <li><svg viewBox="0 0 10 10"><path d="M1 5.5l2.5 2.5L9 1.5" fill="none" stroke="#fff" stroke-width="2"/></svg>Rent Protection</li>
      <li><svg viewBox="0 0 10 10"><path d="M1 5.5l2.5 2.5L9 1.5" fill="none" stroke="#fff" stroke-width="2"/></svg>Equipment Upgrades</li>
      <li><svg viewBox="0 0 10 10"><path d="M1 5.5l2.5 2.5L9 1.5" fill="none" stroke="#fff" stroke-width="2"/></svg>Mast Removals / Decommissioning</li>
      <li><svg viewBox="0 0 10 10"><path d="M1 5.5l2.5 2.5L9 1.5" fill="none" stroke="#fff" stroke-width="2"/></svg>Mast Sales and Marketing</li>
      <li><svg viewBox="0 0 10 10"><path d="M1 5.5l2.5 2.5L9 1.5" fill="none" stroke="#fff" stroke-width="2"/></svg>Land Marketing for Masts</li>
      <li><svg viewBox="0 0 10 10"><path d="M1 5.5l2.5 2.5L9 1.5" fill="none" stroke="#fff" stroke-width="2"/></svg>Mast Management and Portfolios</li>
      <li><svg viewBox="0 0 10 10"><path d="M1 5.5l2.5 2.5L9 1.5" fill="none" stroke="#fff" stroke-width="2"/></svg>Safety Testing</li>
    </ul>
  </div>

  <div class="panel advice">
    <div class="advice__top"></div>
    <h2 class="advice__headline">LANDLORDS SHOULD NOT SIGN ANYTHING UNTIL THEY HAVE SOUGHT PROFESSIONAL ADVICE</h2>
    <div class="advice__brand"><div class="brand"><span class="brand__dot"></span>The Signal Site Company</div></div>
    <p class="advice__prompt">Unsure whether you are getting the best rent?<strong>CALL US NOW FOR A FREE,<br>NO OBLIGATION CHAT</strong></p>
    <div class="contact">
      <p><span class="contact__name">The Signal Site Company Ltd</span><br>The Mill Offices,<br>Kestrel Business Park,<br>Brook Hall,<br>Westshire,<br>WS4 2QP</p>
      <p>t: 01632 960481<br>f: 01632 960482</p>
      <p>e: info@signalsitecompany.co.uk<br>w: www.signalsitecompany.co.uk</p>
    </div>
  </div>

  <div class="panel cover">
    <div class="cover__photo" role="img" aria-label="Photo of a lattice phone mast standing in a green field under a blue sky"></div>
    <div class="cover__brand"><div class="brand brand--sky"><span class="brand__dot"></span>The Signal Site Company</div></div>
    <p class="cover__tagline">We act<br>EXCLUSIVELY<br>for landlords<br>on ALL<br>phone mast<br>matters</p>
    <p class="cover__web">www.signalsitecompany.co.uk</p>
  </div>
</section>

<section class="sheet sheet--inside">
  <div class="panel about">
    <h2 class="about__title">ABOUT US</h2>
    <p class="text about__lead">The Signal Site Company is a firm of telecoms surveyors with over 15 years' experience of dealing with mobile phone mast operators.</p>
    <p class="text about__p1">We have built up a massive database of thousands of comparable mobile phone mast deals to aid us in our telecoms negotiations. All our surveyors have spent time working for phone mast operators and know the industry inside out. We now work exclusively for landlords, fighting your corner, ensuring our landlords get the highest rents and best lease terms available in the market place.</p>
    <p class="text about__p2">Many of the original mobile phone mast leases / agreements are now coming up for renewal. This is an ideal opportunity for landlords to achieve the best deal. We are currently offering to review telecoms leases for free and provide landlords with our recommendations. If you would like to take us up on this free no obligation offer, send a copy of your agreement and any recent correspondence to us, either via post or email using the details on this flyer. Please also provide us with your name, contact number and let us know the current rent you are achieving so we can see if there is room for improvement. Once we have received this, one of our surveyors will give you a call when convenient to talk through your lease with you, highlighting anything we feel needs addressing, any opportunity to increase the rent, or to discuss a specific issue you are having with your mast (i.e. an upgrade request).</p>
  </div>

  <div class="panel middle">
    <p class="text middle__intro">Recently, operators have been attempting to cut costs by reducing rents. They are joining forces in an effort to drive rents down. Many landlords are contacting us after receiving a letter from the operators / operator's agent, telling them they must accept a rent reduction or risk losing their site. In the majority of cases, The Signal Site Company can prevent this from occurring and protect the landlord's rental income.</p>
    <div class="middle__photo" role="img" aria-label="Photo of two surveyors in a field reviewing a laptop"></div>
    <div class="middle__inset" role="img" aria-label="Circular photo of a mast top with antennas against a blue sky"></div>
    <h3 class="heading middle__heading">SELL YOUR PHONE MAST</h3>
    <p class="text middle__sell">We can also assist landlords in selling their phone mast. We have strong links with many large investors who regularly purchase the freehold or leasehold interest of masts and will paya cash lump sum oftens, even hundreds of thousands of pounds. This can be done in a matter of weeks and the cash is yours to spend however you like, regardless of whether the mast stays for the duration of the investors leasehold or not. We can negotiate flexible terms, such as a buyback option so please call us today to discuss.</p>
  </div>

  <div class="panel market">
    <h3 class="heading market__h1">GETTING A PHONE MAST</h3>
    <p class="text market__p1">If you don't currently have a mast located on your land but are interested in receiving thousands of pounds a year in rental income, or you have a redundant mast you would like to market, we offer a free advertising service on our website. We will market your land to phone mast operators with a view to having a mast located there. Please visit the 'Advertise My Site' link on our website to take advantage of this service.</p>
    <h3 class="heading market__h2">THE CURRENT<br>TELECOMS CLIMATE</h3>
    <p class="text market__p2">The telecoms market, in relation to mobile phone masts, is going through some huge changes. Operators are combining to cut costs. We have already seen Kestrel Mobile join forces with Tallis Mobile and Orbit forma jointly owned company with Vantage called Shared Towers Ltd. More recently, Tallis Mobile and Amber have merged to form Allround Networks Ltd to become the new network leader. What this can mean for the landlord is changes to their site and potentially the loss of income. It can all be very confusing but don't worry, this is where we can help. We know the telecoms industry and understand how a new situation may affect a landlord, therefore, allowing us to provide the best advice on protecting your asset.</p>
    <p class="text market__law">In April 2017, the Government introduced the Digital Economy Act. <em>This sets out significant changes for landlords, including the way rents are calculated. We have already seen operators contact landlords, trying to reduce their rent in light of this new law. We are working alongside specialist telecoms solicitors to try to reduce the potential negative impact on landlords.</em></p>
  </div>
</section>

</body>
</html>
```